Business Card Design

we are a wellness center offering therapeutic massage modalities and yoga and meditation classes. I would like to see designs that incorporate the colors of my current logo (image uploaded) BUT I would like to change my logo slightly so that the three words wrapping around my image are: massage yoga wellness (in other words, take out skin).

Industry/Entity Type

Massage

Contact Information for Business Card

Lena R. Calloway, BS, CMT, E-RYT, Owner
427 E. Brindle Ave., Suite 3C
Hampton, VA 23581
757-302-5594 (office)
757-861-2047 (cell)
fernleafrestorative.example
fernleafrestorative@mailbox.example

Requirements
Nice to have
• I'd like to have my logo as a watermark on the back side, but if that's not doable, no big deal. Thanks.

```html
<!DOCTYPE html>
<html lang="en">
<head>
<meta charset="utf-8">
<title>Fernleaf Restorative – Business Cards</title>
<link rel="stylesheet" href="https://fonts.googleapis.com/css2?family=Montserrat:wght@400;500;600&display=swap">
<style>
  :root {
    --backdrop: #efe9df;
    --card: #ffffff;
    --teal: #7fb0b5;
    --coral: #e0643a;
    --coral-soft: #ee8a63;
    --ink: #6b6c70;
    --shadow: rgba(80, 60, 30, 0.18);
  }
  * { box-sizing: border-box; margin: 0; padding: 0; }
  html, body {
    width: 1200px;
    height: 800px;
    overflow: hidden;
    background: var(--backdrop);
    font-family: "Montserrat", Arial, sans-serif;
  }
  .card-set {
    position: absolute;
    inset: 0;
    display: flex;
    align-items: center;
    justify-content: center;
    gap: 50px;
  }
  .card {
    position: relative;
    width: 525px;
    height: 300px;
    background: var(--card);
    border-radius: 4px;
    overflow: hidden;
    box-shadow: 0 10px 30px var(--shadow);
  }
  .card__wave {
    position: absolute;
    inset: 0;
    width: 100%;
    height: 100%;
  }
  .brand {
    position: absolute;
    display: flex;
    align-items: center;
  }
  .brand__dot {
    border-radius: 50%;
    background: var(--teal);
    flex: none;
  }
  .brand__text { display: flex; flex-direction: column; }
  .brand__name {
    color: var(--coral);
    font-weight: 500;
    line-height: 1.1;
  }
  .brand__tagline {
    color: var(--coral);
    font-weight: 600;
    text-transform: uppercase;
    white-space: nowrap;
  }
  /* front side */
  .card--front .brand { left: 24px; top: 44px; gap: 10px; }
  .card--front .brand__dot { width: 56px; height: 56px; }
  .card--front .brand__name { font-size: 20px; }
  .card--front .brand__tagline { font-size: 8.5px; letter-spacing: 0.3px; margin-top: 5px; }
  .card__divider {
    position: absolute;
    left: 252px;
    top: 36px;
    width: 2px;
    height: 170px;
    background: var(--coral);
  }
  .contact {
    position: absolute;
    left: 264px;
    top: 36px;
    font-style: normal;
    color: var(--ink);
    font-size: 12px;
    line-height: 1.6;
  }
  .contact__name { font-weight: 600; }
  .contact__credentials { font-size: 10.5px; font-weight: 500; }
  /* back side */
  .card--back .brand { left: 48px; top: 48px; gap: 20px; }
  .card--back .brand__dot { width: 104px; height: 104px; }
  .card--back .brand__name { font-size: 36px; }
  .card--back .brand__tagline { font-size: 14px; letter-spacing: 0.8px; margin-top: 8px; }
</style>
</head>
<body>
  <main class="card-set">
    <section class="card card--front" aria-label="Card front">
      <svg class="card__wave" viewBox="0 0 525 300" aria-hidden="true">
        <path d="M0,172 C110,140 200,205 300,222 C400,238 460,224 525,246 L525,300 L0,300 Z" fill="var(--coral-soft)"/>
        <path d="M0,188 C120,158 205,222 305,236 C405,250 465,236 525,258 L525,300 L0,300 Z" fill="var(--coral)"/>
      </svg>
      <div class="brand">
        <span class="brand__dot"></span>
        <div class="brand__text">
          <span class="brand__name">Fernleaf<br>Restorative</span>
          <span class="brand__tagline">Massage • Yoga • Wellness</span>
        </div>
      </div>
      <span class="card__divider"></span>
      <address class="contact">
        <div class="contact__name">Lena R. Calloway</div>
        <div class="contact__credentials">BS, CMT, E-RYT, Owner</div>
        <div>427 E. Brindle Ave., Suite 3C</div>
        <div>Hampton, VA 23581</div>
        <div>757-302-5594 (office)</div>
        <div>757-861-2047 (cell)</div>
        <div>fernleafrestorative.example</div>
        <div>fernleafrestorative@mailbox.example</div>
      </address>
    </section>

    <section class="card card--back" aria-label="Card back">
      <svg class="card__wave" viewBox="0 0 525 300" aria-hidden="true">
        <path d="M0,196 C100,168 185,238 290,214 C385,192 445,150 525,172 L525,300 L0,300 Z" fill="var(--coral)"/>
        <path d="M60,250 C150,228 250,262 340,236 C400,218 450,206 500,214 C440,222 400,240 340,252 C250,272 150,246 60,250 Z" fill="var(--card)" opacity="0.9"/>
      </svg>
      <div class="brand">
        <span class="brand__dot"></span>
        <div class="brand__text">
          <span class="brand__name">Fernleaf<br>Restorative</span>
          <span class="brand__tagline">Massage • Yoga • Wellness</span>
        </div>
      </div>
    </section>
  </main>
</body>
</html>
```